Cat-products company needs smart, yet endearing, business card

We need a business card design for a new, but up-and-running, business based in Honolulu, Hawaii. The business is Purrlane Nest Co. Our first product is the most environmentally-friendly cat grass kit ever seen on the planet. Future products, currently in the R&D phase, will include a variety of exciting cat scratchers. We also do consulting work to help apartment-dwellers make their home more cat-friendly and, in the future, plan on doing full, custom installs of structure to create high walkways for cats.

Target Market(s)

Middle-aged, apartment-dwelling, middle-class workers who own 1 or more cats and who dote on them.

Industry/Entity Type

Pet Care

Contact Information for Business Card

A striking, professional, yet warm and friendly design is what we're after.

Font styles to use
Serif
Sans Serif
Other font styles liked:
• Comfortaa

Colors

Designer to choose colors to be used in the design.

Requirements
Must have
• The company logo: (see attachment)
• The company name: Purrlane Nest Co
• The web address: www.purrlanenestco.example
• Email: support@purrlanenestco.example
• Phone: +1 (808) 555 0172
• Update (Fri Jun 30 3017 7:45pm Hawaii Time) I would like, is possible, uploaded picture of the cat grass kit on the back of the card with some text along the lines of: Purrlane Nest Co - Where The Freshest Kitty Sprouts Begin
Nice to have
• A cat picture, cartoon, real or silhouette that illustrates cats in action and/or relaxing; ie using the apartment space to live, play and relax in and being well-contented.
• Most of the website is done in the font: Comfortaa. It might be nice to continue using this for brand consistency.
Should not have
• Hard-to-read fonts.

```html
<!DOCTYPE html>
<html lang="en">
<head>
<meta charset="UTF-8">
<title>Purrlane Nest Co — Business Card</title>
<link rel="stylesheet" href="https://fonts.googleapis.com/css2?family=Comfortaa:wght@500;700&display=swap">
<style>
  :root {
    --page-bg: #eeeeec;
    --card-bg: #ffffff;
    --brand-orange: #f4b41a;
    --brand-brown: #57322a;
    --brand-brown-soft: #6e4236;
  }
  html, body {
    margin: 0;
    padding: 0;
    width: 1200px;
    height: 798px;
    overflow: hidden;
    background: var(--page-bg);
    font-family: "Comfortaa", sans-serif;
  }
  .card {
    position: absolute;
    left: 90px;
    top: 116px;
    width: 1020px;
    height: 565px;
    background: var(--card-bg);
    box-shadow: 0 6px 24px rgba(0, 0, 0, 0.12);
    overflow: hidden;
  }
  .cat-artwork {
    position: absolute;
    left: 0;
    top: 56px;
    width: 236px;
    height: 470px;
    background: linear-gradient(160deg, var(--brand-brown-soft) 0%, var(--brand-brown) 55%);
    border-radius: 0 70% 0 0 / 0 45% 0 0;
  }
  .brand-block {
    position: absolute;
    left: 262px;
    width: 500px;
    top: 0;
    display: flex;
    flex-direction: column;
    align-items: center;
  }
  .brand-square {
    margin-top: 14px;
    width: 64px;
    height: 64px;
    background: var(--brand-brown);
  }
  .brand-name-small {
    margin-top: 12px;
    font-size: 24px;
    font-weight: 700;
    color: var(--brand-orange);
    white-space: nowrap;
  }
  .company-name {
    margin: 38px 0 0;
    font-size: 44px;
    line-height: 1.1;
    font-weight: 700;
    color: var(--brand-orange);
    text-transform: uppercase;
    white-space: nowrap;
    text-shadow: 0 1px 2px rgba(0, 0, 0, 0.12);
  }
  .website {
    margin-top: 4px;
    font-size: 32px;
    font-weight: 500;
    color: var(--brand-orange);
    white-space: nowrap;
  }
  .contact-list {
    position: absolute;
    left: 286px;
    top: 292px;
    margin: 0;
    padding: 0;
    list-style: none;
  }
  .contact-item {
    display: flex;
    align-items: center;
    gap: 14px;
    height: 46px;
    font-size: 25px;
    font-weight: 500;
    color: var(--brand-orange);
    white-space: nowrap;
  }
  .contact-icon {
    width: 22px;
    height: 22px;
    flex: none;
  }
</style>
</head>
<body>
  <main class="card">
    <div class="cat-artwork" role="img" aria-label="Silhouette of a seated cat with its tail stretched along the bottom of the card"></div>

    <div class="brand-block">
      <div class="brand-square"></div>
      <div class="brand-name-small">Purrlane Nest Co</div>
      <h1 class="company-name">Purrlane Nest Co</h1>
      <div class="website">www.purrlanenestco.example</div>
    </div>

    <ul class="contact-list">
      <li class="contact-item">
        <svg class="contact-icon" viewBox="0 0 24 24" aria-hidden="true">
          <rect x="2" y="5" width="20" height="14" rx="1.5" fill="var(--brand-orange)"/>
          <path d="M2.5 6 L12 13 L21.5 6" fill="none" stroke="#ffffff" stroke-width="1.8"/>
        </svg>
        <span>Email: support@purrlanenestco.example</span>
      </li>
      <li class="contact-item">
        <svg class="contact-icon" viewBox="0 0 24 24" aria-hidden="true">
          <path d="M6.6 10.8a15.2 15.2 0 0 0 6.6 6.6l2.2-2.2a1 1 0 0 1 1-.25 11.4 11.4 0 0 0 3.6.57 1 1 0 0 1 1 1V20a1 1 0 0 1-1 1A17 17 0 0 1 3 4a1 1 0 0 1 1-1h3.5a1 1 0 0 1 1 1c0 1.25.2 2.45.57 3.57a1 1 0 0 1-.25 1z" fill="var(--brand-orange)"/>
        </svg>
        <span>Phone: +1 (808) 555 0172</span>
      </li>
    </ul>
  </main>
</body>
</html>
```